A WEBSITE FOR A JEWELLERY RETAIL STORE WITH A SHOPPING CART, AND ABILITY TO ORDER ONLINE.

I require a website with a shopping cart.

We sell MAINLY diamond jewellery (such as rings etc). I need it to be simple to change prices with only a few buttons, as the price fluctuates due to the US Dollar.

We are a diamond wholesaler, selling directly to the public, so we guarantee the lowest prices in Australia.

There is also a link to current inventory that will need to be uploaded to the site.

This could be an ongoing job, where you will be paid weekly to maintain and update the website if you wish.

Target Market(s)

People getting engaged, and wanting to buy a diamond ring.

Number of Pages Required

5+ page

Colors

Designer to choose colors to be used in the design.

Requirements
Must have
• elegant.
• modern.
• professional.
• SHOPPING CART.
• ABILITY TO SEARCH FOR LOOSE DIAMONDS (LINK THAT NEEDS TO BE EMBEDDED WILL BE SENT WHICH SHOWS CURRENT STOCK).
• ENGAGEMENT RINGS
• WEDDING RINGS
• DIAMOND EARRINGS
• DIAMOND PENDANTS
• LOOSE DIAMONDS.
• SALE ITEMS.
• OTHER JEWELLERY.
• EDUCATION
• WISH LIST
• CART.
Nice to have
• a good place to look for inspiration on pages is https://www.lumenvael.example.
• YOU MAY VISIT OUR FACEBOOK PAGE AT.
• HTTP://WWW.SOCIALPAGE.EXAMPLE/QUILLSTONEJEWELLERS
Should not have
• We don't want it too busy.

```html
<!DOCTYPE html>
<html lang="en">
<head>
<meta charset="utf-8">
<title>Quillstone Jewellers</title>
<link href="https://fonts.googleapis.com/css2?family=Lato:wght@300;400;700&family=Playfair+Display:wght@400;700&family=Great+Vibes&display=swap" rel="stylesheet">
<style>
:root{
  --accent:#4a84c4;
  --ink:#2b2b2b;
  --muted:#8a8a8a;
  --line:#e3e3e3;
  --soft:#f6f6f6;
  --footer:#3b4450;
  --footer-text:#b9c0c8;
  --footer-head:#7fb0e6;
  --chip:#5b6572;
  --white:#ffffff;
}
*{margin:0;padding:0;box-sizing:border-box}
html,body{width:1200px;height:2836px;overflow:hidden}
body{position:relative;background:var(--white);font-family:'Lato',sans-serif;color:var(--ink)}
.abs{position:absolute}
.center{left:0;width:1200px;text-align:center}

.topbar{top:0;left:0;width:1200px;height:28px;border-bottom:1px solid var(--line);font-size:10px;color:var(--muted);letter-spacing:1px}
.topbar .left{position:absolute;left:64px;top:8px;display:flex;gap:10px;align-items:center}
.topbar .left .dot{width:8px;height:8px;border-radius:50%;background:#b8b8b8}
.topbar .mid{position:absolute;left:0;width:1200px;text-align:center;top:8px}
.topbar .right{position:absolute;right:64px;top:8px}

.header{top:28px;left:0;width:1200px;height:92px}
.phone{position:absolute;left:64px;top:38px;font-size:13px;color:#555;display:flex;align-items:center;gap:8px}
.brand{position:absolute;left:0;width:1200px;top:22px;text-align:center}
.brand .name{display:block;font-family:'Playfair Display',serif;font-size:30px;font-weight:700;color:#1c1c1c;letter-spacing:2px;line-height:1.1}
.brand .sub{display:block;font-family:'Playfair Display',serif;font-size:10px;font-weight:700;letter-spacing:6px;color:#1c1c1c;margin-top:2px}
.tools{position:absolute;right:64px;top:36px;display:flex;gap:18px}

.nav{top:120px;left:0;width:1200px;height:34px;border-top:1px solid var(--line);border-bottom:1px solid var(--line)}
.nav ul{list-style:none;display:flex;justify-content:space-between;padding:0 150px;line-height:32px;font-size:11px;letter-spacing:1.5px;color:#555}
.nav li.active{color:var(--accent)}

.hero{top:176px;left:68px;width:1064px;height:404px;background:linear-gradient(100deg,#6e5c51 0%,#8f7767 45%,#c7ab92 75%,#e8d5c4 100%)}
.slide-copy{position:absolute;left:96px;top:124px;color:var(--white)}
.script{font-family:'Great Vibes',cursive;font-size:46px;line-height:1}
.script em{font-style:normal;color:#9fc3ea}
.lead{font-size:15px;margin-top:14px;font-weight:300}
.btn{display:inline-block;background:var(--accent);color:var(--white);font-size:10px;letter-spacing:1.5px;padding:9px 18px;border-radius:2px}
.btn.outline{background:var(--white);color:var(--accent);border:1px solid var(--accent)}
.slide-copy .btn{margin-top:26px}
.arrow{position:absolute;top:189px;width:26px;height:26px;border-radius:50%;background:var(--white);display:flex;align-items:center;justify-content:center}

.welcome{top:612px}
.kicker{font-size:10px;letter-spacing:2px;color:var(--muted)}
.heading{font-family:'Playfair Display',serif;font-size:26px;font-weight:700;margin-top:6px}
.para{width:700px;margin:14px auto 0;font-size:11px;line-height:1.7;color:var(--muted)}
.welcome .btn{margin-top:20px}

.collections{top:888px;left:0;width:1200px;height:432px;background:var(--soft)}
.script-title{font-family:'Great Vibes',cursive;font-size:34px;color:var(--ink)}
.rule{display:block;width:160px;height:1px;background:var(--line);margin:6px auto 0}
.cards{position:absolute;top:130px;left:144px;display:flex;gap:24px}
.card{width:210px;text-align:center;font-size:12px;color:#444}
.card .tile{height:186px;border:1px solid var(--line);background:var(--white);padding:8px}
.card .tile div{width:100%;height:100%}
.card p{margin-top:14px}
.card.active p{color:var(--accent);text-decoration:underline}
.collections .more{position:absolute;top:386px;left:0;width:1200px;text-align:center}

.banner{top:1372px;left:68px;width:1064px;height:360px;background:linear-gradient(90deg,#3b352f 0%,#5c5249 45%,#8b7d70 70%,#4b433c 100%)}
.banner .slide-copy{left:70px;top:110px}

.shapes-title{top:1784px}
.shapes{top:1870px;left:106px;width:988px;display:flex;justify-content:space-between}
.shape{width:72px;text-align:center;font-size:11px;color:#555}
.shape svg{display:block;margin:0 auto 14px}
.shapes-btn{top:2012px}

.testimonials{top:2156px}
.quote{font-family:'Playfair Display',serif;font-size:46px;color:var(--accent);line-height:1;margin-top:22px}
.testimonials .para{width:560px;font-size:15px;line-height:1.6;color:#666;margin-top:6px}
.author{font-size:12px;color:var(--accent);margin-top:16px}
.dots{display:flex;justify-content:center;gap:8px;margin-top:20px}
.dots span{width:9px;height:9px;border-radius:50%;background:#ccc}
.dots span.on{background:#888}

.footer{top:2480px;left:0;width:1200px;height:356px;background:var(--footer);color:var(--footer-text);font-size:11px}
.cols{position:absolute;left:152px;top:28px;display:flex}
.col{width:240px;line-height:1.75}
.col h4{color:var(--footer-head);font-weight:400;font-size:13px;margin-bottom:6px}
.col .active{color:var(--footer-head);text-decoration:underline}
.subscribe{display:flex;margin-top:4px}
.subscribe span{width:150px;height:28px;border:1px solid var(--chip)}
.subscribe b{width:28px;height:28px;background:var(--chip)}
.social{display:flex;gap:8px;margin-top:18px}
.social span{width:22px;height:22px;border-radius:50%;background:var(--chip)}
.social span.on{background:var(--accent)}
.copyright{position:absolute;left:152px;bottom:22px;font-size:10px}
.up{position:absolute;right:152px;bottom:16px;width:22px;height:22px;border-radius:50%;background:var(--accent)}
</style>
</head>
<body>

<div class="abs topbar">
  <div class="left">SEE SALE <span class="dot"></span><span class="dot"></span><span class="dot"></span><span class="dot"></span></div>
  <div class="mid">FREE SHIPPING ON ORDERS OVER $100</div>
  <div class="right">MY ACCOUNT</div>
</div>

<header class="abs header">
  <div class="phone">
    <svg width="12" height="12" viewBox="0 0 24 24"><path d="M6 2h4l2 5-3 2a11 11 0 0 0 6 6l2-3 5 2v4a2 2 0 0 1-2 2A18 18 0 0 1 4 4a2 2 0 0 1 2-2z" fill="#777"/></svg>
    +61 400 555 019
  </div>
  <div class="brand">
    <span class="name">QUILLSTONE</span>
    <span class="sub">JEWELLERS</span>
  </div>
  <div class="tools">
    <svg width="16" height="16" viewBox="0 0 24 24" fill="none" stroke="#444" stroke-width="2"><circle cx="10" cy="10" r="7"/><path d="M15 15l6 6"/></svg>
    <svg width="16" height="16" viewBox="0 0 24 24" fill="none" stroke="#444" stroke-width="2"><circle cx="12" cy="8" r="4"/><path d="M4 22c0-5 4-8 8-8s8 3 8 8"/></svg>
    <svg width="16" height="16" viewBox="0 0 24 24" fill="none" stroke="#444" stroke-width="2"><path d="M3 4h3l3 12h11l2-8H7"/><circle cx="10" cy="20" r="1.5"/><circle cx="18" cy="20" r="1.5"/></svg>
  </div>
</header>

<nav class="abs nav">
  <ul>
    <li class="active">ENGAGEMENT RINGS</li><li>WEDDING RINGS</li><li>DIAMOND EARRINGS</li><li>DIAMOND PENDANTS</li><li>LOOSE DIAMONDS</li><li>SALE ITEMS</li>
  </ul>
</nav>

<section class="abs hero" role="img" aria-label="Photograph of a woman wearing a diamond ring and earrings">
  <div class="slide-copy">
    <div class="script">You Design it <em>We Build it</em></div>
    <div class="lead">Create your own Unique Diamond Engagement Ring.</div>
    <span class="btn">VIEW COLLECTION</span>
  </div>
  <div class="arrow" style="left:-13px"><svg width="10" height="10" viewBox="0 0 10 10"><path d="M7 1L3 5l4 4" fill="none" stroke="#333" stroke-width="1.5"/></svg></div>
  <div class="arrow" style="right:-13px;background:var(--accent)"><svg width="10" height="10" viewBox="0 0 10 10"><path d="M3 1l4 4-4 4" fill="none" stroke="#fff" stroke-width="1.5"/></svg></div>
</section>

<section class="abs center welcome">
  <div class="kicker">WELCOME TO</div>
  <div class="heading">Quillstone Jewellers</div>
  <p class="para">Contrary to popular belief, fine jewellery need not cost a fortune. We source every diamond directly and set it by hand in our own workshop, passing wholesale savings on to you. Each piece is made to last a lifetime, crafted with care, certified for quality and backed by our lowest price promise across Australia.</p>
  <span class="btn">SEE SHOP</span>
</section>

<section class="abs collections">
  <div style="text-align:center;padding-top:56px">
    <div class="script-title">Shop By Collections</div>
    <span class="rule"></span>
  </div>
  <div class="cards">
    <div class="card"><div class="tile"><div role="img" aria-label="Diamond engagement rings" style="background:linear-gradient(135deg,#8fd0d4,#bfe4e6)"></div></div><p>Engagement Rings</p></div>
    <div class="card active"><div class="tile"><div role="img" aria-label="Pair of wedding bands" style="background:linear-gradient(135deg,#f3cfc8,#fae6e1)"></div></div><p>Wedding Rings</p></div>
    <div class="card"><div class="tile"><div role="img" aria-label="Gold diamond hoop earrings" style="background:linear-gradient(135deg,#efe6d8,#f8f3ea)"></div></div><p>Diamond Earrings</p></div>
    <div class="card"><div class="tile"><div role="img" aria-label="Gold diamond pendant" style="background:linear-gradient(135deg,#f4f0e8,#fbf9f4)"></div></div><p>Diamond Pendants</p></div>
  </div>
  <div class="more"><span class="btn outline">VIEW ALL COLLECTION</span></div>
</section>

<section class="abs banner" role="img" aria-label="Close-up photograph of a solitaire diamond ring">
  <div class="slide-copy">
    <div class="script">You Design it <em>We Build it</em></div>
    <div class="lead">Create your own Unique Diamond Engagement Ring.</div>
    <span class="btn">SEARCH YOUR DIAMOND</span>
  </div>
</section>

<section class="abs center shapes-title">
  <div class="script-title">Loose Diamonds</div>
  <span class="rule"></span>
</section>

<div class="abs shapes">
  <div class="shape"><svg width="46" height="46" viewBox="0 0 46 46" fill="none" stroke="#555" stroke-width="1.2"><circle cx="23" cy="23" r="20"/><circle cx="23" cy="23" r="10"/></svg>Round</div>
  <div class="shape"><svg width="46" height="46" viewBox="0 0 46 46" fill="none" stroke="#555" stroke-width="1.2"><rect x="4" y="4" width="38" height="38"/><rect x="13" y="13" width="20" height="20"/></svg>Princess</div>
  <div class="shape"><svg width="46" height="46" viewBox="0 0 46 46" fill="none" stroke="#555" stroke-width="1.2"><path d="M12 3h22l9 9v22l-9 9H12l-9-9V12z"/><rect x="14" y="14" width="18" height="18"/></svg>Radiant</div>
  <div class="shape"><svg width="46" height="46" viewBox="0 0 46 46" fill="none" stroke="#555" stroke-width="1.2"><path d="M14 4h18l10 10v18L32 42H14L4 32V14z"/><path d="M18 12h10l6 6v10l-6 6H18l-6-6V18z"/></svg>Asscher</div>
  <div class="shape"><svg width="46" height="46" viewBox="0 0 46 46" fill="none" stroke="#555" stroke-width="1.2"><rect x="4" y="4" width="38" height="38" rx="12"/><rect x="13" y="13" width="20" height="20" rx="5"/></svg>Cushion</div>
  <div class="shape"><svg width="46" height="46" viewBox="0 0 46 46" fill="none" stroke="#555" stroke-width="1.2"><ellipse cx="23" cy="23" rx="14" ry="21"/><ellipse cx="23" cy="23" rx="7" ry="11"/></svg>Oval</div>
  <div class="shape"><svg width="46" height="46" viewBox="0 0 46 46" fill="none" stroke="#555" stroke-width="1.2"><path d="M15 2h16l5 5v32l-5 5H15l-5-5V7z"/><rect x="16" y="10" width="14" height="26"/></svg>Emerald</div>
  <div class="shape"><svg width="46" height="46" viewBox="0 0 46 46" fill="none" stroke="#555" stroke-width="1.2"><path d="M23 2C30 14 37 22 37 30a14 14 0 0 1-28 0c0-8 7-16 14-28z"/><path d="M23 16c3 6 7 10 7 15a7 7 0 0 1-14 0c0-5 4-9 7-15z"/></svg>Pear</div>
  <div class="shape"><svg width="46" height="46" viewBox="0 0 46 46" fill="none" stroke="#555" stroke-width="1.2"><path d="M23 2C33 14 33 32 23 44 13 32 13 14 23 2z"/><path d="M23 14c4 6 4 12 0 18-4-6-4-12 0-18z"/></svg>Marquise</div>
  <div class="shape"><svg width="46" height="46" viewBox="0 0 46 46" fill="none" stroke="#555" stroke-width="1.2"><path d="M23 42L6 24A10 10 0 0 1 23 10a10 10 0 0 1 17 14z"/><path d="M23 32l-8-8a5 5 0 0 1 8-6 5 5 0 0 1 8 6z"/></svg>Heart</div>
</div>

<div class="abs center shapes-btn"><span class="btn outline">SEARCH LOOSE DIAMONDS</span></div>

<section class="abs center testimonials">
  <div class="script-title">Testimonials</div>
  <span class="rule"></span>
  <div class="quote">&ldquo;</div>
  <p class="para">Buying our ring here was simple from start to finish. The team guided us through every stone, and the finished piece is more beautiful than we imagined.</p>
  <div class="author">Hannah Doyle</div>
  <div class="dots"><span></span><span class="on"></span><span></span></div>
</section>

<footer class="abs footer">
  <div class="cols">
    <div class="col">
      <h4>Contact Us</h4>
      Call Us : +61 400 555 019<br>
      hello@quillstone.example<br><br>
      Harbourline Arcade<br>
      18 Wharf Street, Sydney, Australia
    </div>
    <div class="col">
      <h4>Our Collections</h4>
      Engagement Rings<br>
      <span class="active">Wedding Rings</span><br>
      Diamond Earrings<br>
      Diamond Pendants<br>
      Loose Diamonds<br>
      Sale Items
    </div>
    <div class="col">
      <h4>Quick Links</h4>
      About Us<br>
      Education<br>
      Blog<br>
      Contact Us<br>
      Terms &amp; Conditions<br>
      Privacy Policy
    </div>
    <div class="col">
      <h4>Subscribe Us</h4>
      <div class="subscribe"><span></span><b></b></div>
      <div class="social"><span></span><span class="on"></span><span></span><span></span></div>
    </div>
  </div>
  <div class="copyright">&copy; 2024 Quillstone Jewellers. All rights reserved.</div>
  <div class="up"></div>
</footer>

</body>
</html>
```